we are preparing a flyer for an event to promote our new service. to use organge colour as background ( our corporate colour)

Header : Social Media Monitoring, Analytics and Engagement
text :
Leveraging on best of bred technologies, domain knowledge and oversea delivery centres, Tavendra provides social media monitoring, analytic and engagement services.

This can be used for branding, online reputation, social CRM (sales, marketing & customer services), planning & measurement of campaign and research.

Please contact us at contactus@tavendra-example.biz to explore more.

```html
<!DOCTYPE html>
<html lang="en">
<head>
<meta charset="utf-8">
<title>Tavendra – Social Media Monitoring, Analytics and Engagement</title>
<link rel="stylesheet" href="https://fonts.googleapis.com/css2?family=Great+Vibes&family=Fjalla+One&display=swap">
<style>
  :root {
    --yellow-light: #fff23a;
    --yellow: #ffd21a;
    --orange: #f7a21b;
    --orange-deep: #ee8a16;
    --ink: #111111;
    --ghost: rgba(255, 255, 255, 0.38);
    --chip-green: #7fb23a;
    --chip-orange: #f07a1e;
    --chip-red: #b3272a;
    --chip-blue: #2f5f99;
    --chip-crimson: #c9302c;
    --chip-navy: #234d86;
    --chip-sky: #3aa6d8;
    --chip-violet: #b0479a;
    --chip-forest: #3d6b34;
    --chip-ring: #d9d9d9;
  }
  html, body { margin: 0; padding: 0; overflow: hidden; background: #ffffff; }
  .flyer {
    position: relative;
    width: 1200px;
    height: 930px;
    overflow: hidden;
    background: linear-gradient(160deg, var(--yellow-light) 0%, var(--yellow) 35%, var(--orange) 75%, var(--orange-deep) 100%);
    font-family: "Fjalla One", "Arial Narrow", sans-serif;
    color: var(--ink);
  }
  .swooshes { position: absolute; inset: 0; }
  .halftone-globe {
    position: absolute;
    left: -120px; top: 120px;
    width: 820px; height: 820px;
    border-radius: 50%;
    background: radial-gradient(circle at 40% 45%, rgba(255,255,255,0.55) 0%, rgba(255,240,150,0.35) 40%, rgba(255,220,90,0) 70%);
  }
  .ghost-title {
    position: absolute;
    font-family: "Great Vibes", cursive;
    color: var(--ghost);
    white-space: nowrap;
    margin: 0;
    line-height: 1;
  }
  .ghost-1 { left: -10px; top: 40px; font-size: 140px; }
  .ghost-2 { left: 760px; top: 200px; font-size: 130px; }
  .ghost-3 { left: 820px; top: 460px; font-size: 120px; }
  .headline {
    position: absolute; inset: 0; margin: 0;
    font-family: "Great Vibes", cursive;
    font-weight: 400;
    color: var(--ink);
    line-height: 1;
  }
  .headline span { position: absolute; white-space: nowrap; }
  .headline-line-1 { left: 18px; top: 22px; font-size: 92px; }
  .headline-line-2 { left: 628px; top: 178px; font-size: 92px; }
  .headline-line-3 { left: 672px; top: 290px; font-size: 92px; }
  .body-copy {
    position: absolute;
    left: 14px; top: 348px;
    width: 640px;
    font-size: 31px;
    line-height: 38px;
    letter-spacing: 0.3px;
  }
  .body-copy p { margin: 0 0 38px; }
  .contact {
    position: absolute;
    right: 14px; top: 778px;
    margin: 0;
    text-align: right;
    font-size: 31px;
    line-height: 38px;
  }
  .networks {
    position: absolute;
    left: 728px; top: 440px;
    width: 460px;
    display: grid;
    grid-template-columns: repeat(5, 80px);
    column-gap: 15px;
    row-gap: 54px;
    margin: 0; padding: 0; list-style: none;
  }
  .network-chip {
    width: 70px; height: 70px;
    border-radius: 50%;
    border: 5px solid var(--chip-ring);
    display: flex; align-items: center; justify-content: center;
    color: #ffffff;
    font-size: 14px;
    box-sizing: content-box;
  }
  .chip-mail { background: var(--chip-green); }
  .chip-journa { background: var(--chip-orange); }
  .chip-quorix { background: var(--chip-red); }
  .chip-friendo { background: var(--chip-blue); }
  .chip-vidora { background: var(--chip-crimson); }
  .chip-netsy { background: var(--chip-navy); }
  .chip-feeds { background: var(--chip-orange); }
  .chip-chirpa { background: var(--chip-sky); }
  .chip-gabble { background: var(--chip-violet); }
  .chip-linkana { background: var(--chip-forest); }
</style>
</head>
<body>
<main class="flyer">
  <svg class="swooshes" width="1200" height="930" viewBox="0 0 1200 930" aria-hidden="true">
    <path d="M0 60 C 300 -20 700 0 1200 150 L1200 0 L0 0 Z" fill="#f5a623" opacity="0.55"/>
    <path d="M0 250 C 350 120 800 120 1200 60 L1200 150 C 800 200 400 230 0 330 Z" fill="#ffe14d" opacity="0.5"/>
    <path d="M480 930 C 700 700 950 560 1200 520 L1200 930 Z" fill="#f39a1c" opacity="0.85"/>
    <path d="M560 930 C 760 760 980 640 1200 610 L1200 640 C 990 680 790 790 620 930 Z" fill="#ffd84a" opacity="0.6"/>
  </svg>
  <div class="halftone-globe" role="img" aria-label="Soft halftone dot globe pattern"></div>

  <p class="ghost-title ghost-1" aria-hidden="true">al Media Monitoring</p>
  <p class="ghost-title ghost-2" aria-hidden="true">Analytic</p>
  <p class="ghost-title ghost-3" aria-hidden="true">and En</p>

  <h1 class="headline">
    <span class="headline-line-1">Social Media Monitoring,</span>
    <span class="headline-line-2">Analytics</span>
    <span class="headline-line-3">and Engagement</span>
  </h1>

  <section class="body-copy">
    <p>Leveraging on best of bred<br>technologies, domain knowledge<br>and oversea delivery centres,<br>Tavendra provides social media<br>monitoring, analytic and engagement<br>services.</p>
    <p>This can be used for branding, online<br>reputation, social CRM (sales, marketing<br>&amp; customer services), planning &amp;<br>measurement of campaign<br>and research.</p>
  </section>

  <ul class="networks" aria-label="Channels covered">
    <li class="network-chip chip-mail" aria-label="Email">
      <svg width="44" height="30" viewBox="0 0 44 30" aria-hidden="true">
        <rect x="1" y="1" width="42" height="28" fill="#ffffff" stroke="#6b8f2e" stroke-width="2"/>
        <path d="M1 1 L22 17 L43 1" fill="none" stroke="#6b8f2e" stroke-width="2"/>
      </svg>
    </li>
    <li class="network-chip chip-journa">Journa</li>
    <li class="network-chip chip-quorix">Quorix</li>
    <li class="network-chip chip-friendo">Friendo</li>
    <li class="network-chip chip-vidora">Vidora</li>
    <li class="network-chip chip-netsy">Netsy</li>
    <li class="network-chip chip-feeds">Feeds</li>
    <li class="network-chip chip-chirpa">Chirpa</li>
    <li class="network-chip chip-gabble">Gabble</li>
    <li class="network-chip chip-linkana">Linkana</li>
  </ul>

  <p class="contact">Please contact us at<br>contactus@tavendra-example.biz<br>to explore more.</p>
</main>
</body>
</html>
```